Business Card Design for Miss Poppy's Soak Parlour

Name: Miss Poppy's Soak Parlour. Maker of bath bombs, bath salts.

Card details:

Donna Pickett
1.702.555.0143
Las Vegas Nevada
dpickett47@mailpost.example

"Bath bombs, bath salts and more..."

A picture of an old-fashioned bathtub (with claw feet) filled with bath bombs.

Colors include: Lavender, Pink, Turquois, Light Blue. Can you make the overall design look old fashioned.

```html
<!DOCTYPE html>
<html lang="en">
<head>
<meta charset="utf-8">
<title>Miss Poppy's Soak Parlour – Business Card</title>
<link rel="stylesheet" href="https://fonts.googleapis.com/css2?family=Open+Sans:wght@700&family=Roboto:wght@400;700&display=swap">
<style>
  :root {
    --page-bg: #ffffff;
    --card-purple: #652d8e;
    --card-text: #ffffff;
  }
  html, body {
    margin: 0;
    padding: 0;
    width: 1200px;
    height: 900px;
    overflow: hidden;
    background: var(--page-bg);
  }
  .canvas {
    position: relative;
    width: 1200px;
    height: 900px;
  }
  .business-card {
    position: absolute;
    left: 351px;
    top: 310px;
    width: 506px;
    height: 289px;
    background: var(--card-purple);
    color: var(--card-text);
  }
  .brand {
    position: absolute;
    left: 205px;
    top: 98px;
    width: 280px;
    text-align: center;
    font-family: "Open Sans", sans-serif;
    font-weight: 700;
  }
  .brand-name {
    margin: 0;
    font-size: 19px;
    letter-spacing: -0.3px;
    line-height: 1.2;
  }
  .brand-tagline {
    margin: 5px 0 0;
    font-size: 12.5px;
    letter-spacing: -0.2px;
    line-height: 1.2;
  }
  .owner-name {
    position: absolute;
    left: 28px;
    top: 206px;
    margin: 0;
    font-family: "Roboto", sans-serif;
    font-weight: 700;
    font-size: 22px;
    letter-spacing: -0.3px;
  }
  .contact-list {
    position: absolute;
    left: 254px;
    top: 203px;
    margin: 0;
    padding: 0;
    list-style: none;
    font-family: "Roboto", sans-serif;
    font-size: 16px;
    line-height: 21px;
  }
  .contact-item {
    display: flex;
    align-items: center;
    gap: 6px;
    white-space: nowrap;
  }
  .contact-icon {
    width: 12px;
    height: 12px;
    fill: var(--card-text);
    flex: none;
  }
</style>
</head>
<body>
<main class="canvas">
  <section class="business-card" aria-label="Business card for Miss Poppy's Soak Parlour">
    <header class="brand">
      <h1 class="brand-name">Miss Poppy's Soak Parlour</h1>
      <p class="brand-tagline">"Bath bombs, bath salts and more...</p>
    </header>

    <p class="owner-name">Donna Pickett</p>

    <ul class="contact-list">
      <li class="contact-item">
        <svg class="contact-icon" viewBox="0 0 24 24" aria-hidden="true">
          <path d="M6.6 10.8c1.4 2.8 3.8 5.1 6.6 6.6l2.2-2.2c.3-.3.7-.4 1-.2 1.1.4 2.3.6 3.6.6.6 0 1 .4 1 1V20c0 .6-.4 1-1 1C10.6 21 3 13.4 3 4c0-.6.4-1 1-1h3.5c.6 0 1 .4 1 1 0 1.3.2 2.5.6 3.6.1.3 0 .7-.2 1l-2.3 2.2z"/>
        </svg>
        <span>1.702.555.0143</span>
      </li>
      <li class="contact-item">
        <svg class="contact-icon" viewBox="0 0 24 24" aria-hidden="true">
          <path d="M12 2C8.1 2 5 5.1 5 9c0 5.2 7 13 7 13s7-7.8 7-13c0-3.9-3.1-7-7-7zm0 9.5a2.5 2.5 0 1 1 0-5 2.5 2.5 0 0 1 0 5z"/>
        </svg>
        <span>Las Vegas Nevada</span>
      </li>
      <li class="contact-item">
        <svg class="contact-icon" viewBox="0 0 24 24" aria-hidden="true">
          <path d="M2 5h20v14H2z"/>
        </svg>
        <span>dpickett47@mailpost.example</span>
      </li>
    </ul>
  </section>
</main>
</body>
</html>
```